German Headhunter/ HR Consultancy needs Business Cards Design

We need a business Card Design for our Company in Stuttgart. We are specialized as Headhunter/ HR Consultancy in Placement of specialist and managers in permanent employment. Please refer to our business logo.

```html
<!DOCTYPE html>
<html lang="de">
<head>
<meta charset="utf-8">
<title>Nordwerk Personalberatung – Visitenkarte</title>
<link href="https://fonts.googleapis.com/css2?family=Montserrat:wght@600;700&family=Quicksand:wght@500;600&display=swap" rel="stylesheet">
<style>
  :root {
    --brand-blue: #3953a6;
    --brand-blue-light: #4a65b5;
    --accent-grey: #a3a4a7;
    --paper: #ffffff;
    --ink: #2b2b2b;
    --stage: #2b2b2d;
  }
  * { margin: 0; padding: 0; box-sizing: border-box; }
  html, body { width: 1200px; height: 1120px; overflow: hidden; background: var(--stage); }
  .stage { position: relative; width: 1200px; height: 1120px; }

  .card {
    position: absolute; left: 220px; width: 760px; height: 460px;
    border-radius: 26px; overflow: hidden;
  }
  .card--front { top: 70px; background: var(--paper); }
  .card--back { top: 590px; background: linear-gradient(135deg, var(--brand-blue) 0%, var(--brand-blue-light) 100%); }

  /* front */
  .front-strip { position: absolute; left: 0; top: 0; width: 78px; height: 100%; background: var(--brand-blue); }
  .front-strip__grey { position: absolute; left: 0; top: 0; width: 78px; height: 120px; background: var(--accent-grey); }
  .front-decor { position: absolute; right: 0; top: 0; width: 250px; height: 460px; }

  .wordmark { position: absolute; left: 120px; top: 62px; display: flex; align-items: center; gap: 14px; }
  .wordmark__square { width: 40px; height: 40px; background: var(--brand-blue); }
  .wordmark__text {
    font-family: "Montserrat", sans-serif; font-weight: 700; color: var(--brand-blue);
    line-height: 1;
  }
  .wordmark__name { font-size: 40px; letter-spacing: 1px; display: block; }
  .wordmark__sub { font-size: 15px; letter-spacing: 2.4px; display: block; margin-top: 4px; }

  .person { position: absolute; left: 120px; top: 200px; }
  .person__name { font-family: "Montserrat", sans-serif; font-weight: 700; font-size: 30px; color: var(--brand-blue); }
  .person__role { font-family: "Quicksand", sans-serif; font-weight: 600; font-size: 17px; color: var(--ink); margin-top: 2px; }

  .contact { position: absolute; left: 120px; top: 290px; list-style: none;
    font-family: "Quicksand", sans-serif; font-weight: 500; font-size: 17px; color: var(--ink); }
  .contact__item { display: flex; align-items: center; gap: 12px; height: 30px; }
  .contact__icon { width: 16px; height: 16px; fill: var(--brand-blue); flex: none; }

  /* back */
  .back-decor { position: absolute; left: 0; top: 0; width: 760px; height: 460px; }
  .back-wordmark {
    position: absolute; right: 80px; top: 100px; text-align: left;
    font-family: "Montserrat", sans-serif; font-weight: 700; color: var(--paper); line-height: 1;
  }
  .back-wordmark__name { display: block; font-size: 92px; letter-spacing: 3px; }
  .back-wordmark__sub { display: block; font-size: 33px; letter-spacing: 3px; margin-top: 10px; }
</style>
</head>
<body>
<main class="stage">

  <section class="card card--front" aria-label="Vorderseite der Visitenkarte">
    <div class="front-strip"><div class="front-strip__grey"></div></div>
    <svg class="front-decor" viewBox="0 0 250 460" aria-hidden="true">
      <polygon points="110,0 250,0 250,210" fill="var(--brand-blue)"/>
      <polygon points="250,250 250,330 170,460 120,460" fill="var(--brand-blue)"/>
    </svg>

    <div class="wordmark">
      <span class="wordmark__square"></span>
      <span class="wordmark__text">
        <span class="wordmark__name">NORDWERK</span>
        <span class="wordmark__sub">PERSONALBERATUNG</span>
      </span>
    </div>

    <div class="person">
      <p class="person__name">Jonas Berger</p>
      <p class="person__role">Geschäftsführer</p>
    </div>

    <ul class="contact">
      <li class="contact__item">
        <svg class="contact__icon" viewBox="0 0 16 16"><path d="M3 1l3 3-1.5 2a9 9 0 0 0 5.5 5.5L12 10l3 3-2 2C6 15 1 10 1 3z"/></svg>
        +49 1520 4417309
      </li>
      <li class="contact__item">
        <svg class="contact__icon" viewBox="0 0 16 16"><path d="M1 3h14v10H1z M2 4l6 5 6-5" fill="var(--brand-blue)" stroke="#fff" stroke-width="1"/></svg>
        kontakt@nordwerk-personal.de
      </li>
      <li class="contact__item">
        <svg class="contact__icon" viewBox="0 0 16 16"><circle cx="8" cy="8" r="7"/><path d="M1 8h14M8 1c-3 4-3 10 0 14M8 1c3 4 3 10 0 14" stroke="#fff" stroke-width="1" fill="none"/></svg>
        www.nordwerk-personal.de
      </li>
      <li class="contact__item">
        <svg class="contact__icon" viewBox="0 0 16 16"><path d="M8 1a5 5 0 0 1 5 5c0 4-5 9-5 9S3 10 3 6a5 5 0 0 1 5-5z"/><circle cx="8" cy="6" r="2" fill="#fff"/></svg>
        Lindenweg 14, 70174 Stuttgart, Germany
      </li>
    </ul>
  </section>

  <section class="card card--back" aria-label="Rückseite der Visitenkarte">
    <svg class="back-decor" viewBox="0 0 760 460" aria-hidden="true">
      <polygon points="0,290 0,460 320,460" fill="var(--paper)"/>
      <polygon points="0,365 0,460 180,460" fill="var(--brand-blue)"/>
    </svg>
    <div class="back-wordmark">
      <span class="back-wordmark__name">NORDWERK</span>
      <span class="back-wordmark__sub">PERSONALBERATUNG</span>
    </div>
  </section>

</main>
</body>
</html>
```